LKND - Ledgers Kept Neatly Daily

We need a business card design for a company located in Australia - accounting / tax firm.

2 sided business card - I have attached a one-sided concept that I did in MSWord :) If anything it shows that I want a striking design - bold, fresh and less reserved than your average accounting firm's card.

Rather than having all the info on the front, maybe it could just have name and logo on front?

Want to keep colours in line with logo - orange, black and white.

Happy for full colour. Will be using a matte finish.

About Us (below)
LKND does business, and more specifically accounting and taxation differently.
People require news and other media at their fingertips so why should business figures and documents be any different?
In combination with Quilo, a cloud based accounting package, we store all receipts, tax returns and special documentation with a secure online data-storage provider and provide you with your own login. We are also interested to hear if video conferencing is something you would be interested in.
Using this technology we are able to focus more on your business and less on the data entry.

Target Market(s)

Individual mum and dad clients, and Small to Medium Business

Industry/Entity Type

Accounting

Requirements
Must have
• Must be able to edit the details at a future point in time ie - phone, address, website address, name on card and slogan.

2 sided

Standard Australian business card size
Nice to have
• Rather than having all the info on the front, maybe it could just have name and logo on front?
Should not have
• Don't want "Ledgers Kept Neatly Daily" on the card

```html
<!DOCTYPE html>
<html lang="en">
<head>
<meta charset="utf-8">
<title>LKND Business Card</title>
<link rel="stylesheet" href="https://fonts.googleapis.com/css2?family=Michroma&family=Open+Sans:wght@400&display=swap">
<style>
  :root {
    --orange: #e77a1a;
    --orange-mark: #ee8b27;
    --dark-1: #343434;
    --dark-2: #161616;
    --white: #ffffff;
    --page: #ffffff;
  }
  html, body {
    margin: 0;
    padding: 0;
    width: 1200px;
    height: 900px;
    overflow: hidden;
    background: var(--page);
  }
  .canvas {
    position: relative;
    width: 1200px;
    height: 900px;
  }
  .card {
    position: absolute;
    left: 251px;
    width: 660px;
    height: 396px;
    overflow: hidden;
    background: radial-gradient(ellipse at 55% 45%, var(--dark-1) 0%, #262626 55%, var(--dark-2) 100%);
    box-shadow: 0 0 2px rgba(0,0,0,0.25);
  }
  .card--front { top: 42px; }
  .card--back { top: 462px; }

  .front-panel {
    position: absolute;
    left: 0; top: 0;
    width: 330px; height: 100%;
    background: var(--orange);
  }

  .brand-mark {
    position: absolute;
    width: 144px; height: 144px;
    border-radius: 50%;
    background: var(--orange-mark);
  }
  .card--front .brand-mark { left: 259px; top: 122px; }
  .card--back .brand-mark { left: 342px; top: 108px; }

  .brand {
    position: absolute;
    text-align: right;
    font-family: "Open Sans", sans-serif;
    color: var(--white);
  }
  .card--front .brand { right: 421px; top: 150px; }
  .card--back .brand { right: 338px; top: 128px; }
  .brand-name {
    display: block;
    font-size: 56px;
    line-height: 64px;
    letter-spacing: -1px;
  }
  .brand-services {
    display: block;
    font-size: 17px;
    line-height: 21px;
  }

  .person {
    position: absolute;
    right: 34px; top: 66px;
    text-align: right;
    font-family: "Michroma", sans-serif;
  }
  .person-name {
    display: block;
    color: var(--orange);
    font-size: 24px;
    font-variant: small-caps;
    letter-spacing: 3px;
    line-height: 32px;
  }
  .person-title {
    display: block;
    color: var(--white);
    font-size: 14px;
    letter-spacing: 2px;
    line-height: 20px;
  }

  .contact-list {
    position: absolute;
    right: 32px; top: 232px;
    margin: 0; padding: 0;
    list-style: none;
    font-family: "Michroma", sans-serif;
    font-size: 13px;
    color: var(--white);
    letter-spacing: 2px;
  }
  .contact-item {
    display: flex;
    justify-content: flex-end;
    align-items: baseline;
    height: 25px;
  }
  .contact-item--email { height: 27px; }
  .contact-label {
    color: var(--orange);
    font-size: 11px;
    margin-right: 16px;
    font-variant: small-caps;
  }
  .contact-label--at { font-size: 15px; font-family: "Open Sans", sans-serif; }
  .contact-value { font-variant: small-caps; }
  .contact-address { text-align: right; line-height: 22px; }

  .back-rule {
    position: absolute;
    left: 34px; top: 339px;
    width: 592px; height: 3px;
    background: var(--orange);
  }
  .website {
    position: absolute;
    left: 0; right: 0; top: 357px;
    text-align: center;
    font-family: "Michroma", sans-serif;
    font-size: 11px;
    letter-spacing: 2.5px;
    color: var(--white);
  }
</style>
</head>
<body>
<main class="canvas">
  <section class="card card--front" aria-label="Card front">
    <div class="front-panel"></div>
    <div class="brand-mark" aria-hidden="true"></div>
    <div class="brand">
      <span class="brand-name">LKND</span>
      <span class="brand-services">Bookeeping</span>
      <span class="brand-services">Accounting</span>
      <span class="brand-services">Taxation</span>
    </div>
    <div class="person">
      <span class="person-name">Daniel Reed</span>
      <span class="person-title">TAX AGENT</span>
    </div>
    <ul class="contact-list">
      <li class="contact-item"><span class="contact-label">p</span><span class="contact-value">0412.555.018</span></li>
      <li class="contact-item"><span class="contact-label">f</span><span class="contact-value">0412.555.018</span></li>
      <li class="contact-item"><span class="contact-label">c</span><span class="contact-value">0412.555.018</span></li>
      <li class="contact-item contact-item--email"><span class="contact-label contact-label--at">@</span><span class="contact-value">reed@lknd.com.au</span></li>
      <li class="contact-item"><span class="contact-label">a</span><span class="contact-value contact-address">1820 - 41 St.<br>Ridgeway, AB</span></li>
    </ul>
  </section>

  <section class="card card--back" aria-label="Card back">
    <div class="brand-mark" aria-hidden="true"></div>
    <div class="brand">
      <span class="brand-name">LKND</span>
      <span class="brand-services">Bookeeping</span>
      <span class="brand-services">Accounting</span>
      <span class="brand-services">Taxation</span>
    </div>
    <div class="back-rule"></div>
    <div class="website">WWW.LKND.COM.AU</div>
  </section>
</main>
</body>
</html>
```